Wordpress website for voluntary transgender support online

We need a website as an information support for transgender people and their friends and families. We are a self funded voluntary support group reaching out to educate all in need.
Fairly basic site. Tabs for 3 of us to put bios, professional resources and contacts, news, general information, our contact info, entertainment.
Our logo is attached and we'd love the use of clouds and the colour lilac. We wish to look professional but approachable and personable.

Target Market(s)

Transgender people,mr heir families and friends and general public.

Industry/Entity Type

Group

Requirements
Must have
• Willow 4 logo.
• Tabs for: about us, contacts, news, bios x3, suggestions, professional resources, entertainment, personal resources, general information.
• We are hoping to set up in Wordpress so that we can then manage the page and update in the future.
• Coding will be required.
Nice to have
• Any suggestions.

```html
<!DOCTYPE html>
<html lang="en">
<head>
<meta charset="utf-8">
<title>Willow 4 – Transgender and Crossdressing Support Group</title>
<link href="https://fonts.googleapis.com/css2?family=Open+Sans:wght@400;600;700&family=Raleway:wght@400;600;700&display=swap" rel="stylesheet">
<style>
:root{
  --lilac:#6f4fa3;
  --lilac-dark:#553a85;
  --ink:#333338;
  --muted:#8a8a8f;
  --line:#e4e4e8;
  --paper:#ffffff;
  --soft:#f6f6f8;
  --night:#2b2b30;
  --footer:#3a3a3e;
  --footer-bottom:#2e2e32;
}
*{box-sizing:border-box;margin:0;padding:0}
html,body{width:1200px;height:2704px;overflow:hidden;background:var(--paper)}
body{font-family:'Open Sans',Arial,sans-serif;color:var(--ink);font-size:14px;line-height:1.6}
h1,h2,h3,h4{font-family:'Raleway',Arial,sans-serif}

.site-header{height:80px;display:flex;align-items:center;justify-content:space-between;padding:0 60px}
.brand{display:flex;flex-direction:column;align-items:center;color:var(--lilac);font-family:'Raleway',sans-serif}
.brand-mark{width:26px;height:26px;border-radius:50%;background:var(--lilac);margin-bottom:2px}
.brand-name{font-size:20px;font-weight:600;line-height:1}
.brand-tag{font-size:8px;letter-spacing:2px;color:var(--muted)}
.main-nav{display:flex;gap:46px;font-size:11px;font-weight:600;letter-spacing:.5px}
.main-nav a{color:var(--ink);text-decoration:none}

.hero{position:relative;height:472px;background:linear-gradient(100deg,#c9b7a8 0%,#a79385 35%,#8c8078 60%,#b9b3ad 100%)}
.hero-photo{position:absolute;inset:0}
.hero-copy{position:absolute;left:676px;top:148px;color:#fff}
.hero-copy h1{font-size:40px;font-weight:700;letter-spacing:1px;line-height:1.15}
.hero-copy p{font-family:'Raleway',sans-serif;font-size:26px;line-height:1.3;margin-top:4px;width:420px}
.btn{display:inline-block;background:var(--lilac);color:#fff;font-size:11px;font-weight:600;letter-spacing:1px;padding:10px 26px;text-decoration:none}
.hero-copy .btn{margin-top:22px}

.section-title{text-align:center;font-size:28px;font-weight:700;letter-spacing:.5px}
.section-lead{text-align:center;color:var(--muted);font-size:12px;width:820px;margin:14px auto 0}

.welcome{padding-top:52px;height:420px}
.features{display:grid;grid-template-columns:repeat(4,1fr);gap:40px;padding:0 80px;margin-top:70px}
.feature-head{display:flex;gap:14px;align-items:flex-start}
.feature-head svg{flex:none}
.feature h3{font-size:13px;font-weight:700;color:var(--ink);line-height:1.3}
.feature p{font-size:11px;color:var(--muted);margin-top:14px}

.projects{height:460px;padding-top:0}
.project-grid{display:grid;grid-template-columns:repeat(4,242px);gap:16px;justify-content:center;margin-top:36px}
.project-img{height:160px}
.project h4{font-size:11px;text-align:center;margin-top:14px;font-weight:700}
.project p{font-size:10px;color:var(--muted);text-align:center}
.dots{display:flex;justify-content:center;gap:8px;margin-top:26px}
.dots span{width:7px;height:7px;border-radius:50%;background:#ccc}
.dots span.on{background:var(--lilac)}

.what-we-do{height:300px;background:linear-gradient(90deg,#2a2a2f,#3d3b40 50%,#29292d);color:#fff;text-align:center;padding-top:50px}
.what-we-do h2{font-size:30px;font-weight:700}
.what-we-do p{font-size:12px;color:#d3d3d8;width:860px;margin:16px auto 0}
.btn-ghost{display:inline-block;border:1px solid #fff;color:#fff;font-size:11px;letter-spacing:1px;padding:10px 26px;margin-top:28px;text-decoration:none}

.testimonials{height:520px;position:relative;padding:60px 0 0 100px}
.testimonials h2{font-size:26px;font-weight:700}
.testimonials .rule{width:46px;height:3px;background:var(--lilac);margin-top:10px}
.quote{display:flex;gap:18px;margin-top:60px;width:520px}
.quote-mark{font-family:'Raleway',sans-serif;font-size:60px;color:#cfc6dc;line-height:.8}
.quote p{font-size:12px;color:var(--muted)}
.quote-author{margin:26px 0 0 58px}
.quote-author strong{color:var(--lilac);font-size:13px;display:block}
.quote-author span{font-size:11px;color:var(--muted)}
.client-photo{position:absolute;right:120px;top:70px;width:380px;height:410px;background:radial-gradient(circle at 50% 40%,#f2f2f2,#d8d8dc 70%)}

.partners{height:100px;display:flex;justify-content:space-around;align-items:center;padding:0 80px}
.partner{width:110px;height:34px;border-radius:4px;background:#e6e2ec}

.site-footer{height:288px;background:var(--footer);color:#cfcfd3;display:grid;grid-template-columns:300px 400px 250px 250px;padding:40px 0 0 60px}
.footer-brand{display:flex;flex-direction:column;align-items:center;width:180px;margin-top:24px;color:#bdbdc2}
.footer-brand .brand-mark{background:#9b9ba0;width:34px;height:34px}
.footer-brand .brand-name{font-size:26px}
.site-footer h4{font-size:12px;font-weight:700;color:#fff;margin-bottom:14px;letter-spacing:.5px}
.site-footer p,.site-footer li{font-size:11px;line-height:1.9;color:#aeaeb3}
.site-footer ul{list-style:none}
.site-footer .mission p{width:340px}
.more{color:#fff;font-size:11px;margin-top:10px;display:block}
.contact-line{display:flex;gap:10px;align-items:center}
.bottom-bar{height:64px;background:var(--footer-bottom);display:flex;align-items:center;justify-content:space-between;padding:0 60px;font-size:10px;color:#8e8e93}
.socials{display:flex;gap:18px;align-items:center;white-space:nowrap}
.socials-label{font-size:10px;color:#8e8e93;margin-right:8px}
.social-dot{width:9px;height:9px;border-radius:50%;background:#7a7a80;flex:none}
</style>
</head>
<body>

<header class="site-header">
  <div class="brand">
    <span class="brand-mark"></span>
    <span class="brand-name">willowfour</span>
    <span class="brand-tag">SUPPORT GROUP</span>
  </div>
  <nav class="main-nav">
    <a href="#">HOME</a><a href="#">ABOUT US</a><a href="#">BIOS</a><a href="#">NEWS</a><a href="#">SUGGESTIONS</a><a href="#">RESOURCES</a><a href="#">CONTACT US</a>
  </nav>
</header>

<section class="hero">
  <div class="hero-photo" role="img" aria-label="Smiling woman with long hair working at a laptop in a bright room"></div>
  <div class="hero-copy">
    <h1>WILLOW 4 IS A</h1>
    <p>FREE TRANSGENDER AND CROSSDRESSING SUPPORT GROUP</p>
    <a class="btn" href="#">CLICK HERE FOR MORE</a>
  </div>
</section>

<section class="welcome">
  <h2 class="section-title">WELCOME TO WILLOW 4</h2>
  <p class="section-lead">Willow 4 is a free Transgender and crossdressing support group committed to providing support and understanding to the transgender. Crossdresser and gender diverse group including their partners, family and friends to Willow 4 you will find a "like minded" people with real life experiences and a passion to help whoever the life.</p>
  <div class="features">
    <div class="feature">
      <div class="feature-head">
        <svg width="24" height="24" viewBox="0 0 24 24"><circle cx="12" cy="12" r="5" fill="none" stroke="#6f4fa3" stroke-width="3"/><path d="M12 2v4M12 18v4M2 12h4M18 12h4M5 5l3 3M16 16l3 3M5 19l3-3M16 8l3-3" stroke="#6f4fa3" stroke-width="2.4"/></svg>
        <h3>SUPPORT<br>AND SERVICES</h3>
      </div>
      <p>Lorem Ipsum is simply dummy text of the printing and typesetting industry. Lorem Ipsum has been the industry's standard dummy.</p>
    </div>
    <div class="feature">
      <div class="feature-head">
        <svg width="26" height="22" viewBox="0 0 26 22"><rect x="3" y="2" width="20" height="13" fill="none" stroke="#6f4fa3" stroke-width="2"/><rect x="0" y="17" width="26" height="3" fill="#6f4fa3"/></svg>
        <h3>INFORMATION<br>AND CONTACT</h3>
      </div>
      <p>Lorem Ipsum is simply dummy text of the printing and typesetting industry. Lorem Ipsum has been the industry's standard dummy.</p>
    </div>
    <div class="feature">
      <div class="feature-head">
        <svg width="26" height="22" viewBox="0 0 26 22"><path d="M13 2L1 8l12 6 12-6z" fill="#6f4fa3"/><path d="M6 11v5c4 3 10 3 14 0v-5" fill="none" stroke="#6f4fa3" stroke-width="2"/></svg>
        <h3>EDUCATION<br>AND AWARENESS</h3>
      </div>
      <p>Lorem Ipsum is simply dummy text of the printing and typesetting industry. Lorem Ipsum has been the industry's standard dummy.</p>
    </div>
    <div class="feature">
      <div class="feature-head">
        <svg width="24" height="24" viewBox="0 0 24 24"><path d="M4 10a8 8 0 0 1 14-4M20 14a8 8 0 0 1-14 4" fill="none" stroke="#6f4fa3" stroke-width="2.4"/><path d="M18 1v6h-6M6 23v-6h6" fill="none" stroke="#6f4fa3" stroke-width="2.4"/></svg>
        <h3>UNNECESSARY AND<br>UNACCEPTABLE</h3>
      </div>
      <p>Lorem Ipsum is simply dummy text of the printing and typesetting industry. Lorem Ipsum has been the industry's standard dummy.</p>
    </div>
  </div>
</section>

<section class="projects">
  <h2 class="section-title">RECENT PROJECTS</h2>
  <p class="section-lead">Willow 4 is a free Transgender and crossdressing support group committed to providing support and understanding to the transgender. Crossdresser and gender diverse group including their partners.</p>
  <div class="project-grid">
    <div class="project"><div class="project-img" role="img" aria-label="Blue cloud computing concept image" style="background:linear-gradient(135deg,#9fc3e0,#4d7fb0)"></div><h4>LOREM IPSUM IS SIMPLY DUMMY</h4><p>Click here for more details</p></div>
    <div class="project"><div class="project-img" role="img" aria-label="Business handshake over a desk" style="background:linear-gradient(135deg,#3f5e86,#a9b6c6)"></div><h4>LOREM IPSUM IS SIMPLY DUMMY</h4><p>Click here for more details</p></div>
    <div class="project"><div class="project-img" role="img" aria-label="Team meeting around a table" style="background:linear-gradient(135deg,#7e98ad,#d5dbe0)"></div><h4>LOREM IPSUM IS SIMPLY DUMMY</h4><p>Click here for more details</p></div>
    <div class="project"><div class="project-img" role="img" aria-label="Hand pointing at charts on a tablet" style="background:linear-gradient(135deg,#4f86bd,#c8dcec)"></div><h4>LOREM IPSUM IS SIMPLY DUMMY</h4><p>Click here for more details</p></div>
  </div>
  <div class="dots"><span class="on"></span><span></span><span></span><span></span></div>
</section>

<section class="what-we-do" role="img" aria-label="Dark background photo of people in a meeting">
  <h2>WHAT WE DO</h2>
  <p>Willow 4 is a free Transgender and crossdressing support group committed to providing support and understanding to the transgender. Crossdresser and gender diverse group including their partners, family and friends at Willow 4 you will find "like minded" people with real life experiences and a passion to help.</p>
  <a class="btn-ghost" href="#">CLICK HERE FOR MORE</a>
</section>

<section class="testimonials">
  <h2>WHAT OUR CLIENT'S SAY</h2>
  <div class="rule"></div>
  <div class="quote">
    <span class="quote-mark">&ldquo;</span>
    <p>Lorem Ipsum is simply dummy text of the printing and typesetting industry. Lorem Ipsum has been the industry's standard dummy text ever since the 1500s, when an unknown printer took a galley of type and scrambled it.</p>
  </div>
  <div class="quote-author"><strong>Martin Hale</strong><span>Business man</span></div>
  <div class="client-photo" role="img" aria-label="Portrait of a man in a suit resting his chin on his hand"></div>
</section>

<section class="partners" aria-label="Partners">
  <span class="partner"></span><span class="partner"></span><span class="partner"></span><span class="partner"></span><span class="partner"></span><span class="partner"></span>
</section>

<footer class="site-footer">
  <div class="footer-brand">
    <span class="brand-mark"></span>
    <span class="brand-name">willowfour</span>
  </div>
  <div class="mission">
    <h4>OUR MISSION</h4>
    <p>Willow 4 is a free Transgender and crossdressing support group committed to providing support and understanding to the Transgender, crossdresser and gender diverse group including their partners, family and friends.</p>
    <a class="more" href="#">Read more info &rsaquo;</a>
  </div>
  <div>
    <h4>WELCOME</h4>
    <ul><li>About Us</li><li>Bios</li><li>News</li><li>Suggestions</li><li>Resources</li><li>Contact Us</li></ul>
  </div>
  <div>
    <h4>CONTACT INFO</h4>
    <p>12 Harbour Lane, Fernvale<br>Central District 4021</p>
    <p class="contact-line">+00 1234 5678</p>
    <p class="contact-line">hello@willowfour.org</p>
  </div>
</footer>
<div class="bottom-bar">
  <span>&copy; 2015 Willow 4. All Rights Reserved</span>
  <div class="socials"><span class="socials-label">Let's stay in touch</span><span class="social-dot"></span><span class="social-dot"></span><span class="social-dot"></span><span class="social-dot"></span><span class="social-dot"></span></div>
</div>

</body>
</html>
```